TLB Shark card

This is a serious business card for a retired attorney with a sarcastic sense of humor. Incorporate into the design: shark with the tag line, Harmless unless provoked. The image could be graphic but not comic. The card should have a classic, sophisticated, professional look. Partial to minimalist, even Asian designs. Color options are black/ white (though this can easily go too cartoonish), gray tones, blue gray tones, blue. Open to something unexpected, even color, as long as the look is professional. The shark image attached is what we've been using but it isn't a design requirement.(Not sure why entire image isn't visible.)
Updates

No company Howard L Brisbane Name should be more prominent than the tag

This is the first time I've done this, so I apologize for not posting all this info up front. Some of it was in the narrative but to make it easier, I'm listing all the info that should be on the card. Howard L Brisbane Attorney at Law shark image Harmless unless provoked 27815 Velvet Harbor Street Dana Point, CA 92631 555-814-2073 hbrisbane@quellmail.net There is no company. The tag, Harmless unless provoked, should be less prominent than the name.

Industry/Entity Type

Attorney

Contact Information for Business Card

27815 Velvet Harbor Street
Dana Point, CA 92631
555-814-2073
hbrisbane@quellmail.net

```html
<!DOCTYPE html>
<html lang="en">
<head>
<meta charset="utf-8">
<title>TLB Shark card</title>
<link href="https://fonts.googleapis.com/css2?family=Exo+2:wght@300;400;500&display=swap" rel="stylesheet">
<style>
  :root {
    --backdrop: #5c5c5c;
    --card-black: #0d0d0d;
    --card-black-soft: #1c1c1c;
    --ink-white: #f4f4f4;
    --ink-gray: #9a9a9a;
    --panel-white: #ffffff;
    --edge-blue: #2a3a7a;
    --art-light: #d9d9d9;
    --art-dark: #3a3a3a;
  }
  * { margin: 0; padding: 0; box-sizing: border-box; }
  html, body {
    width: 1200px; height: 800px; overflow: hidden;
    background: var(--backdrop);
    font-family: "Exo 2", sans-serif;
  }
  .sheet {
    position: relative; width: 1200px; height: 800px;
    display: flex; align-items: center; justify-content: center; gap: 60px;
  }
  .card {
    position: relative; width: 525px; height: 300px;
    border-radius: 22px; overflow: hidden;
    background: var(--card-black);
    box-shadow: 0 14px 30px rgba(0,0,0,0.45);
  }

  /* Front */
  .card-front .shark-art {
    position: absolute; left: 215px; top: 34px; width: 120px; height: 72px;
    border-radius: 6px;
    background: linear-gradient(120deg, var(--art-dark), #8a8a8a 55%, var(--art-dark));
    opacity: 0.8;
  }
  .card-front .details {
    position: absolute; left: 120px; right: 24px; top: 114px;
  }
  .tagline-small {
    margin-left: 40px;
    font-weight: 400; font-size: 12px; letter-spacing: 3px; white-space: nowrap;
    color: var(--ink-gray); text-transform: uppercase;
  }
  .name {
    margin-top: 4px;
    font-weight: 500; font-size: 31px; letter-spacing: 2.5px; white-space: nowrap;
    color: var(--ink-white); text-transform: uppercase; line-height: 1.1;
  }
  .contact-list { list-style: none; margin-top: 12px; }
  .contact-list li {
    display: flex; align-items: center; gap: 10px; white-space: nowrap;
    font-weight: 400; font-size: 13px; color: var(--ink-white);
    line-height: 1.75;
  }
  .contact-list svg { width: 12px; height: 12px; fill: var(--ink-white); flex: none; }

  /* Back */
  .card-back {
    background: radial-gradient(ellipse at 40% 50%, var(--card-black-soft), var(--card-black) 75%);
  }
  .card-back .corner-panel {
    position: absolute; inset: 0; width: 100%; height: 100%;
  }
  .card-back .shark-art {
    position: absolute; left: 150px; top: 60px; width: 220px; height: 130px;
    border-radius: 8px;
    background: linear-gradient(120deg, #2a2a2a, var(--art-light) 55%, #2a2a2a);
    opacity: 0.75;
  }
  .tagline-large {
    position: absolute; left: 30px; width: 420px; top: 218px; text-align: center;
    font-weight: 400; font-size: 19px; letter-spacing: 5px; white-space: nowrap;
    color: var(--ink-white); text-transform: uppercase;
  }
</style>
</head>
<body>
<main class="sheet">

  <section class="card card-front" aria-label="Business card front">
    <div class="shark-art" role="img" aria-label="Gray brush-line shark illustration"></div>
    <div class="details">
      <p class="tagline-small">Gentle until crossed</p>
      <h1 class="name">Howard L Brisbane</h1>
      <ul class="contact-list">
        <li>
          <svg viewBox="0 0 12 12" aria-hidden="true"><path d="M6 0.5a4 4 0 0 0-4 4c0 3 4 7 4 7s4-4 4-7a4 4 0 0 0-4-4zm0 5.5a1.5 1.5 0 1 1 0-3 1.5 1.5 0 0 1 0 3z"/></svg>
          27815 Velvet Harbor Street Dana Point, CA 92631
        </li>
        <li>
          <svg viewBox="0 0 12 12" aria-hidden="true"><path d="M2.5 1h2l1 2.6-1.3 1a7 7 0 0 0 3.2 3.2l1-1.3L11 7.5v2A1.5 1.5 0 0 1 9.5 11 8.5 8.5 0 0 1 1 2.5 1.5 1.5 0 0 1 2.5 1z"/></svg>
          555-814-2073
        </li>
        <li>
          <svg viewBox="0 0 12 12" aria-hidden="true"><path d="M0.5 2h11v8h-11zM1.5 3l4.5 3.5L10.5 3v-0.2H1.5z"/></svg>
          hbrisbane@quellmail.net
        </li>
      </ul>
    </div>
  </section>

  <section class="card card-back" aria-label="Business card back">
    <svg class="corner-panel" viewBox="0 0 525 300" preserveAspectRatio="none" aria-hidden="true">
      <path d="M330 0 L525 0 L525 230 Z" fill="var(--panel-white)"/>
      <path d="M330 0 L525 230" stroke="var(--edge-blue)" stroke-width="1.5" fill="none"/>
    </svg>
    <div class="shark-art" role="img" aria-label="White brush-line shark illustration"></div>
    <p class="tagline-large">Gentle until crossed</p>
  </section>

</main>
</body>
</html>
```